Investment Business - Biz Card Design

Using the attached logo files, please create a superior business card design for Tarnwell Holdings.

The "back" of the card should feature the logo (either in colour, or white/black over a feature colour)

The "front" of the card should feature: name, email, and phone

The design should be minimal and clean.

Target Market(s)

Business owners who need our investment services.

Industry/Entity Type

Business

```html
<!DOCTYPE html>
<html lang="en">
<head>
<meta charset="utf-8">
<title>Tarnwell Holdings – Business Card</title>
<link href="https://fonts.googleapis.com/css2?family=Montserrat:wght@400;500;700&display=swap" rel="stylesheet">
<style>
  :root {
    --brand-blue: #27a4dd;
    --brand-navy: #2b3a8f;
    --card-white: #ffffff;
    --stage-bg: #2a2a2c;
  }
  * { margin: 0; padding: 0; box-sizing: border-box; }
  html, body {
    width: 1200px;
    height: 900px;
    overflow: hidden;
    background: var(--stage-bg);
    font-family: "Montserrat", sans-serif;
  }
  .card-set {
    position: relative;
    width: 1200px;
    height: 900px;
    display: flex;
    justify-content: center;
    align-items: center;
    gap: 80px;
  }
  .card {
    position: relative;
    width: 400px;
    height: 700px;
    overflow: hidden;
    box-shadow: 0 12px 30px rgba(0, 0, 0, 0.45);
  }

  /* Front */
  .card-front { background: var(--card-white); }
  .card-front .identity {
    position: absolute;
    left: 44px;
    right: 40px;
    top: 318px;
  }
  .company-name {
    display: flex;
    align-items: center;
    gap: 12px;
    font-weight: 700;
    font-size: 27px;
    letter-spacing: 0.5px;
    color: var(--brand-navy);
    line-height: 1;
    white-space: nowrap;
  }
  .company-name .mark-square {
    width: 18px;
    height: 18px;
    background: var(--brand-blue);
    flex: none;
  }
  .divider {
    height: 2px;
    background: var(--brand-blue);
    margin: 22px 0 18px;
  }
  .person-name {
    font-weight: 700;
    font-size: 21px;
    letter-spacing: 1.5px;
    color: var(--brand-navy);
    text-transform: uppercase;
    margin-bottom: 12px;
  }
  .contact-list {
    list-style: none;
    font-weight: 500;
    font-size: 14px;
    letter-spacing: 0.8px;
    line-height: 1.5;
    color: var(--brand-blue);
  }
  .footer-band {
    position: absolute;
    left: 0;
    right: 0;
    bottom: 0;
    height: 84px;
    background: var(--brand-blue);
  }

  /* Back */
  .card-back {
    background: var(--brand-blue);
    display: flex;
    align-items: center;
    justify-content: center;
  }
  .card-back .company-name {
    color: var(--card-white);
    font-size: 30px;
  }
  .card-back .company-name .mark-square { background: var(--card-white); }
</style>
</head>
<body>
  <main class="card-set">
    <section class="card card-front" aria-label="Card front">
      <div class="identity">
        <div class="company-name"><span class="mark-square"></span>Tarnwell Holdings</div>
        <div class="divider"></div>
        <h1 class="person-name">Evan Tarrow</h1>
        <ul class="contact-list">
          <li>email: evan@tarnwellholdings.com</li>
          <li>web: tarnwellholdings.com</li>
          <li>phone: 555 - 0142 - 7730</li>
        </ul>
      </div>
      <div class="footer-band"></div>
    </section>

    <section class="card card-back" aria-label="Card back">
      <div class="company-name"><span class="mark-square"></span>Tarnwell Holdings</div>
    </section>
  </main>
</body>
</html>
```